Medical group practice

We need a flyer design incorporating the three doctors in the practice, there is a general practitioner, ophthalmologist and an obstetrician & Gynaecologist. see the attached file for the concept. will leave the colour design up to you

Target Market(s)

general public

Industry/Entity Type

Health Care

Colors

Designer to choose colors to be used in the design.

Requirements
Must have
• logos included in attachement

```html
<!DOCTYPE html>
<html lang="en">
<head>
<meta charset="utf-8">
<title>Coralvale Medical – Flyer</title>
<link href="https://fonts.googleapis.com/css2?family=Exo+2:wght@600;700&family=Lato:ital,wght@0,400;0,700;1,400&display=swap" rel="stylesheet">
<style>
  :root {
    --red: #d8202f;
    --grey: #6d6d6d;
    --text: #2b2b2b;
    --muted: #555;
    --gp-blue: #1f6fb3;
    --eye-purple: #7b1f7a;
    --ob-green: #1a9150;
    --navy: #1d3b8a;
    --rule: #e3e3e3;
    --page: #ece8e2;
  }
  * { box-sizing: border-box; margin: 0; padding: 0; }
  html, body { width: 1200px; height: 1200px; overflow: hidden; background: var(--page); }
  body { font-family: "Lato", sans-serif; color: var(--text); }

  .flyer {
    position: absolute; left: 155px; top: 24px;
    width: 990px; height: 1280px; background: #fff;
    transform: scale(0.9); transform-origin: top left;
    overflow: hidden;
  }
  .abs { position: absolute; }

  .hero-art { position: absolute; left: 0; top: 0; }

  .brand { left: 0; width: 420px; top: 0; text-align: center; }
  .brand-mark { position: absolute; left: 170px; top: 90px; width: 74px; height: 74px; border-radius: 50%; background: var(--red); }
  .brand-name { position: absolute; left: 34px; top: 250px; font-weight: 700; font-size: 31px; letter-spacing: .5px; color: var(--red); white-space: nowrap; }
  .tagline { position: absolute; left: 35px; top: 288px; width: 344px; display: flex; align-items: center; gap: 8px; font-size: 20px; font-weight: 700; color: var(--muted); white-space: nowrap; }
  .tagline::before, .tagline::after { content: ""; flex: 1; height: 2px; background: var(--muted); }
  .hotline { position: absolute; left: 66px; top: 340px; display: flex; align-items: center; gap: 10px; font-size: 25px; color: #444; white-space: nowrap; }

  .doctor { position: absolute; left: 0; width: 990px; }
  .clinic-mark { position: absolute; left: 40px; display: flex; align-items: center; gap: 10px; font-weight: 700; font-size: 15px; width: 200px; white-space: nowrap; }
  .clinic-mark .dot { flex: none; width: 22px; height: 22px; border-radius: 50%; }
  .doc-name { position: absolute; left: 249px; font-family: "Exo 2", sans-serif; font-weight: 700; font-size: 21px; white-space: nowrap; }
  .doc-role { position: absolute; left: 249px; font-size: 16px; line-height: 20px; color: var(--text); white-space: nowrap; }
  .doc-role.italic { font-style: italic; }
  .doc-mail { position: absolute; left: 249px; display: flex; align-items: center; gap: 8px; font-size: 16px; white-space: nowrap; }

  .services { position: absolute; list-style: none; font-size: 16px; line-height: 22.6px; white-space: nowrap; }
  .services li { position: relative; padding-left: 23px; }
  .services li::before { content: ""; position: absolute; left: 0; top: 4px; width: 13px; height: 13px; border: 1.5px solid #555; border-radius: 50%; }
  .services li::after { content: ""; position: absolute; left: 4.5px; top: 7px; width: 3px; height: 6px; border: solid #555; border-width: 0 1.5px 1.5px 0; transform: rotate(45deg); }
  .services-head { position: absolute; font-family: "Exo 2", sans-serif; font-weight: 700; font-size: 17px; color: var(--navy); white-space: nowrap; }

  .rule { position: absolute; left: 40px; width: 910px; height: 1px; background: var(--rule); }

  .footer-art { position: absolute; left: 0; top: 1085px; }
  .contact { position: absolute; left: 34px; list-style: none; color: #fff; font-size: 16px; font-weight: 700; white-space: nowrap; }
  .contact li { display: flex; align-items: center; gap: 8px; height: 23px; }
  .contact .address { margin-bottom: 12px; }
  .hours { position: absolute; left: 645px; top: 1180px; display: flex; align-items: center; gap: 14px; }
  .hours h2 { font-size: 21px; font-weight: 700; color: #222; }
  .hours p { font-size: 18px; line-height: 23px; color: #222; white-space: nowrap; }
</style>
</head>
<body>
<main class="flyer">

  <svg class="hero-art" width="990" height="560" viewBox="0 0 990 560">
    <defs>
      <linearGradient id="heroFade" x1="0" y1="0" x2="1" y2="1">
        <stop offset="0" stop-color="#f4f6f8"/>
        <stop offset=".5" stop-color="#dfe8ef"/>
        <stop offset="1" stop-color="#eef2f5"/>
      </linearGradient>
      <linearGradient id="heroLeft" x1="0" y1="0" x2="1" y2="0">
        <stop offset="0" stop-color="#ffffff"/>
        <stop offset="1" stop-color="#f3f4f5"/>
      </linearGradient>
    </defs>
    <rect x="0" y="0" width="990" height="560" fill="url(#heroLeft)"/>
    <rect role="img" aria-label="Photo of four smiling doctors in white coats and scrubs with stethoscopes and clipboards" x="400" y="30" width="590" height="520" fill="url(#heroFade)"/>
    <path d="M0,468 C150,420 300,455 430,515 C540,560 720,560 860,460 C930,410 970,350 990,300 L990,560 L0,560 Z" fill="#fff"/>
    <path d="M0,450 C140,418 290,430 420,480" fill="none" stroke="var(--grey)" stroke-width="9"/>
    <path d="M0,470 C150,430 300,455 430,515 C540,560 720,560 860,460 C930,410 970,350 990,300 L990,330 C960,410 910,470 840,510 C700,575 520,565 400,520 C270,470 130,470 0,500 Z" fill="var(--red)"/>
    <path d="M0,515 C120,490 240,490 340,510" fill="none" stroke="var(--grey)" stroke-width="5"/>
    <path d="M990,420 L990,548 C960,520 930,500 880,490 C930,470 970,450 990,420 Z" fill="#9a9a9a"/>
  </svg>

  <header class="brand abs">
    <div class="brand-mark"></div>
    <h1 class="brand-name">CORALVALE MEDICAL</h1>
    <p class="tagline">Your Health is our Priority</p>
    <p class="hotline">
      <svg width="26" height="26" viewBox="0 0 24 24"><circle cx="12" cy="12" r="11" fill="none" stroke="var(--red)" stroke-width="1.5"/><path d="M8 6.5l2 2-1.2 1.6c.8 1.8 2.3 3.3 4.1 4.1l1.6-1.2 2 2-1.4 1.8c-4.2-.6-8.3-4.7-8.9-8.9z" fill="var(--red)"/></svg>
      (555) 014 2270 / 2271
    </p>
  </header>

  <!-- General practitioner -->
  <section class="doctor" style="top:0">
    <div class="clinic-mark" style="top:620px; color:var(--gp-blue)"><span class="dot" style="background:var(--gp-blue)"></span>Holloway Clinic</div>
    <h3 class="doc-name" style="top:600px; color:var(--gp-blue)">Dr. Everett Holloway, MD.</h3>
    <p class="doc-role italic" style="top:630px">General Practitioner</p>
    <p class="doc-mail" style="top:660px">
      <svg width="24" height="16" viewBox="0 0 24 16"><rect x="1" y="1" width="22" height="14" rx="2" fill="none" stroke="var(--gp-blue)" stroke-width="1.5"/><path d="M1 2l11 8 11-8M1 15l8-6M23 15l-8-6" fill="none" stroke="var(--gp-blue)" stroke-width="1.3"/></svg>
      e.holloway.doc@example.com
    </p>
    <ul class="services" style="left:543px; top:597px">
      <li>General Checks</li><li>Annual Check ups</li><li>Wound Care/Dressings</li><li>Incision &amp; Drainage</li>
    </ul>
    <ul class="services" style="left:770px; top:597px">
      <li>Suturing lacerations</li><li>Pain Injections</li><li>Glucose checks</li><li>Foreign Body Removal</li>
    </ul>
  </section>

  <div class="rule" style="top:737px"></div>

  <!-- Ophthalmologist -->
  <section class="doctor" style="top:0">
    <div class="clinic-mark" style="top:800px; color:var(--eye-purple)"><span class="dot" style="background:var(--eye-purple)"></span>ClearView Eye Services</div>
    <h3 class="doc-name" style="top:774px; color:var(--eye-purple)">Dr. Lucinda R. Valdez</h3>
    <p class="doc-role italic" style="top:803px">MD. Surgeon Ophthalmologist</p>
    <p class="doc-mail" style="top:834px">
      <svg width="24" height="16" viewBox="0 0 24 16"><rect x="1" y="1" width="22" height="14" rx="2" fill="none" stroke="var(--gp-blue)" stroke-width="1.5"/><path d="M1 2l11 8 11-8M1 15l8-6M23 15l-8-6" fill="none" stroke="var(--gp-blue)" stroke-width="1.3"/></svg>
      lucinda.eyes@example.com
    </p>
    <ul class="services" style="left:543px; top:774px">
      <li>Eyes disease examination,</li><li>Surgery of Pterygium</li><li>Cataract,</li><li>Glaucoma</li>
    </ul>
    <h4 class="services-head" style="left:771px; top:773px">Emergency:</h4>
    <ul class="services" style="left:770px; top:797px">
      <li>Conjunctivitis,</li><li>Traumatism</li><li>Foreign body and more</li>
    </ul>
  </section>

  <div class="rule" style="top:908px"></div>

  <!-- Obstetrician & Gynaecologist -->
  <section class="doctor" style="top:0">
    <div class="clinic-mark" style="top:990px; color:var(--navy)"><span class="dot" style="background:var(--ob-green)"></span>Ramsaran Women's Care</div>
    <h3 class="doc-name" style="left:251px; top:941px; color:var(--ob-green)">Dr. Julian Ramsaran</h3>
    <p class="doc-role" style="left:251px; top:969px">BMedSci, MBBS, DM (O&amp;G), FACOG<br>Obstetrician &amp; Gynaecologist</p>
    <p class="doc-mail" style="left:251px; top:1023px">
      <svg width="24" height="16" viewBox="0 0 24 16"><rect x="1" y="1" width="22" height="14" rx="2" fill="none" stroke="var(--gp-blue)" stroke-width="1.5"/><path d="M1 2l11 8 11-8M1 15l8-6M23 15l-8-6" fill="none" stroke="var(--gp-blue)" stroke-width="1.3"/></svg>
      drramsaran@example.com
    </p>
    <h4 class="services-head" style="left:545px; top:941px">Gynaecology :</h4>
    <ul class="services" style="left:543px; top:967px">
      <li>Pap smears</li><li>Abnormal vaginal bleeding</li><li>Fibroids</li><li>Colposcopy</li><li>Family planning</li><li>Infertility</li><li>Cancer screening</li><li>And More….</li>
    </ul>
    <h4 class="services-head" style="left:771px; top:941px">Obstetrics :</h4>
    <ul class="services" style="left:770px; top:967px">
      <li>Prenatal Care</li><li>Delivery</li><li>Postnatal checks</li><li>High Risk pregnancy</li>
    </ul>
  </section>

  <svg class="footer-art" width="990" height="195" viewBox="0 0 990 195">
    <path d="M0,22 C170,2 320,20 470,80" fill="none" stroke="var(--grey)" stroke-width="7"/>
    <path d="M0,40 C170,20 330,45 480,110 C520,130 545,148 560,195 L0,195 Z" fill="var(--red)"/>
    <path d="M540,132 C680,82 830,56 990,46" fill="none" stroke="var(--red)" stroke-width="3"/>
    <path d="M730,60 C820,44 910,37 990,34" fill="none" stroke="var(--grey)" stroke-width="7"/>
    <path d="M560,195 C700,180 850,172 990,162 L990,195 Z" fill="var(--red)"/>
  </svg>

  <ul class="contact" style="top:1148px">
    <li class="address">
      <svg width="18" height="22" viewBox="0 0 18 22"><path d="M9 1a7 7 0 0 0-7 7c0 5 7 13 7 13s7-8 7-13a7 7 0 0 0-7-7z" fill="none" stroke="#fff" stroke-width="2"/><circle cx="9" cy="8" r="2.5" fill="#fff"/></svg>
      42 Harbour Lane, Port Mercy
    </li>
    <li><svg width="18" height="18" viewBox="0 0 24 24"><circle cx="12" cy="12" r="11" fill="none" stroke="#fff" stroke-width="1.5"/><path d="M8 6.5l2 2-1.2 1.6c.8 1.8 2.3 3.3 4.1 4.1l1.6-1.2 2 2-1.4 1.8c-4.2-.6-8.3-4.7-8.9-8.9z" fill="#fff"/></svg>General Practitioner - (555) 013 4418,</li>
    <li><svg width="18" height="18" viewBox="0 0 24 24"><circle cx="12" cy="12" r="11" fill="none" stroke="#fff" stroke-width="1.5"/><path d="M8 6.5l2 2-1.2 1.6c.8 1.8 2.3 3.3 4.1 4.1l1.6-1.2 2 2-1.4 1.8c-4.2-.6-8.3-4.7-8.9-8.9z" fill="#fff"/></svg>Ophthalmologist - (555) 017 0932,</li>
    <li><svg width="18" height="18" viewBox="0 0 24 24"><circle cx="12" cy="12" r="11" fill="none" stroke="#fff" stroke-width="1.5"/><path d="M8 6.5l2 2-1.2 1.6c.8 1.8 2.3 3.3 4.1 4.1l1.6-1.2 2 2-1.4 1.8c-4.2-.6-8.3-4.7-8.9-8.9z" fill="#fff"/></svg>Obstetrician/Gynaecologist – (555) 019 6620, (555) 012 8847</li>
  </ul>

  <div class="hours">
    <svg width="58" height="58" viewBox="0 0 58 58"><circle cx="29" cy="29" r="26" fill="none" stroke="#555" stroke-width="3"/><circle cx="29" cy="29" r="20" fill="none" stroke="#555" stroke-width="1"/><path d="M29 14v15l9 7" fill="none" stroke="#555" stroke-width="3" stroke-linecap="round"/></svg>
    <div>
      <h2>OPENING HOURS :</h2>
      <p>Monday – Fridays : 9am-6pm<br>Saturdays :10am – 5pm</p>
    </div>
  </div>

</main>
</body>
</html>
```